Business Card Design/Logo

I require a design/logo for my own Company, Morvix. The Jewellery I make is totally hand crafted. I own a hand Mining Claim out in the gemfields of Queensland and dig up my own stones. I also fossick for Gold Locally so all my Jewellery products are hand dug/cut/created. Quality stones are hand cut by my partner (Faceted) and other stones (Seconds) are either skin polished or recessed into pieces of Solid 925 Silver or Solid 9ct and 18 ct Gold. I make Sets (Collections) or just one-of designs. All the stones come in different colours and I am now starting to use different colour Golds. The final design should radiate professionalism, quality and uniqueness.

Target Market(s)

Many designs will cost a minimum of AU Dollars $2,000

Industry/Entity Type

Business

Contact Information for Business Card

Morvix Creations
Distinct Bench Wrought Native Adornments
0400327986
P.O. Box 418 Ambercrest 4719 Qld
morvixgarnets@mailbrook.net

```html
<!DOCTYPE html>
<html lang="en">
<head>
<meta charset="utf-8">
<title>Morvix Creations — Business Card</title>
<link href="https://fonts.googleapis.com/css2?family=Marcellus&family=Questrial&family=Open+Sans:wght@400;700&display=swap" rel="stylesheet">
<style>
  :root {
    --backdrop: #1a1a1c;
    --card: #f7f7f5;
    --ink: #1c1c1c;
    --ink-soft: #2e2e2e;
    --silver: #b9bcc2;
  }
  * { margin: 0; padding: 0; box-sizing: border-box; }
  html, body {
    width: 1200px; height: 800px; overflow: hidden;
    background: var(--backdrop);
  }
  .canvas {
    position: relative; width: 1200px; height: 800px;
    display: flex; align-items: center; justify-content: center;
  }
  .business-card {
    position: relative; width: 880px; height: 503px;
    background: var(--card);
    color: var(--ink);
  }
  .brand {
    position: absolute; left: 96px; top: 92px;
    display: flex; align-items: flex-start; gap: 30px;
  }
  .brand-mark {
    width: 58px; height: 58px; margin-top: 6px;
    background: var(--silver);
  }
  .brand-name {
    font-family: "Marcellus", serif;
    font-size: 64px; line-height: 1; letter-spacing: 2px;
    color: var(--ink);
  }
  .brand-tagline {
    font-family: "Questrial", sans-serif;
    font-size: 19px; letter-spacing: 0.5px;
    color: var(--ink-soft); margin-top: 12px;
  }
  .holder {
    position: absolute; right: 96px; top: 232px; text-align: right;
    font-family: "Open Sans", sans-serif;
  }
  .holder-name { font-weight: 700; font-size: 18px; letter-spacing: 0.3px; }
  .holder-role { font-size: 15px; color: var(--ink-soft); margin-top: 2px; }
  .contact {
    position: absolute; left: 110px; bottom: 62px;
    font-family: "Open Sans", sans-serif;
    font-size: 17px; line-height: 1.45; color: var(--ink-soft);
    list-style: none;
  }
  .contact-label { font-weight: 700; color: var(--ink); margin-right: 4px; }
</style>
</head>
<body>
  <main class="canvas">
    <section class="business-card" aria-label="Morvix Creations business card">
      <header class="brand">
        <div class="brand-mark" aria-hidden="true"></div>
        <div class="brand-text">
          <h1 class="brand-name">MORVIX</h1>
          <p class="brand-tagline">Creations · Unique · Hand Made</p>
        </div>
      </header>

      <div class="holder">
        <p class="holder-name">LENA HARTWELL</p>
        <p class="holder-role">Founder &amp; CEO</p>
      </div>

      <ul class="contact">
        <li><span class="contact-label">T:</span>0400327986</li>
        <li><span class="contact-label">E:</span>morvixgarnets@mailbrook.net</li>
        <li>P.O. Box 418 Ambercrest, 4719 Qld</li>
      </ul>
    </section>
  </main>
</body>
</html>
```